Harlow Grading and Septic needs a flyer to submit to contractors to offer our services

I need a sleek profession one page full color high gloss document showcasing our services to give to Mobile Home Companies and contractors that need our services.

Home Builders. Mobile Home Salesmen. People Building new homes.

Construction

Serif
Sans Serif

• Phone Number. Email address. Logo. Services offered: Mobile Home Pads, Meter Pole Placement and Connection, Waterline Connection, On Site Septic System Installs
• Jokes, Nothing trying to be cute

```html
<!DOCTYPE html>
<html lang="en">
<head>
<meta charset="utf-8">
<title>Harlow Grading and Septic – Contractor Flyer</title>
<link rel="stylesheet" href="https://fonts.googleapis.com/css2?family=Oswald:wght@500;600;700&family=Jost:wght@500&family=Poppins:wght@400;600&display=swap">
<style>
  :root{
    --backdrop:#8a8a8a;
    --paper:#ffffff;
    --light-gray:#e4e4e4;
    --mid-gray:#d6d6d6;
    --navy:#1d4f91;
    --deep-navy:#173f78;
    --brand-red:#8c1f25;
    --bright-red:#c4202b;
    --signal-yellow:#fff200;
    --white:#ffffff;
    --text-dark:#1f2a36;
  }
  html,body{margin:0;padding:0;width:1200px;height:2408px;overflow:hidden;background:var(--backdrop);}
  .flyer{position:absolute;left:50px;top:426px;width:1100px;height:1556px;overflow:hidden;background:var(--paper);}
  .flyer-art{position:absolute;inset:0;width:1100px;height:1556px;display:block;}

  .brand{position:absolute;left:52px;top:62px;width:522px;text-align:center;font-family:"Oswald",sans-serif;font-weight:700;color:var(--navy);}
  .brand-name{margin:0;line-height:1;text-transform:uppercase;}
  .brand-name .line-1{display:block;font-size:96px;letter-spacing:6px;}
  .brand-name .line-2{display:block;font-size:54px;letter-spacing:1px;margin-top:6px;}
  .brand-phone{display:block;margin-top:14px;font-size:34px;letter-spacing:4px;font-weight:600;}

  .headline{position:absolute;left:52px;top:690px;margin:0;color:var(--white);line-height:1;}
  .headline .row{display:block;white-space:nowrap;}
  .headline .plain{font-family:"Jost",sans-serif;font-weight:500;font-size:86px;}
  .headline .accent{font-family:"Oswald",sans-serif;font-weight:700;font-size:88px;color:var(--signal-yellow);}
  .headline .row-2{margin-top:8px;}
  .headline .tagline{font-family:"Jost",sans-serif;font-weight:500;font-size:72px;margin-top:14px;letter-spacing:1px;}

  .services{position:absolute;left:340px;top:1100px;width:720px;color:var(--white);font-family:"Poppins",sans-serif;}
  .services-title{margin:0 0 0 30px;width:500px;text-align:center;font-weight:600;font-size:42px;padding-bottom:10px;border-bottom:2px solid var(--white);}
  .service-list{list-style:none;margin:18px 0 0;padding:0;font-size:32px;line-height:1.12;}
  .service-list li{position:relative;padding-left:46px;margin-bottom:10px;}
  .service-list li:nth-child(1){margin-left:105px;}
  .service-list li:nth-child(2){margin-left:85px;}
  .service-list li:nth-child(3){margin-left:60px;}
  .service-list li:nth-child(4){margin-left:38px;}
  .tick{position:absolute;left:0;top:6px;width:30px;height:28px;}

  .contact{position:absolute;left:240px;top:1470px;display:flex;align-items:center;font-family:"Oswald",sans-serif;color:var(--deep-navy);}
  .contact-icon{width:40px;height:40px;margin-right:20px;}
  .contact-phone{font-weight:500;font-size:42px;margin-right:50px;}
  .contact-web{font-weight:600;font-size:26px;}
</style>
</head>
<body>
<main class="flyer">
  <svg class="flyer-art" viewBox="0 0 1100 1556" aria-hidden="false">
    <defs>
      <linearGradient id="gray-site" x1="0" y1="0" x2="1" y2="1">
        <stop offset="0" stop-color="#b9b9b9"/><stop offset="0.5" stop-color="#8f8f8f"/><stop offset="1" stop-color="#c8c8c8"/>
      </linearGradient>
      <linearGradient id="tank-site" x1="0" y1="0" x2="0" y2="1">
        <stop offset="0" stop-color="#4d6a3a"/><stop offset="0.5" stop-color="#c9c6bf"/><stop offset="1" stop-color="#a88a62"/>
      </linearGradient>
      <linearGradient id="sky-site" x1="0" y1="0" x2="0" y2="1">
        <stop offset="0" stop-color="#2f63b8"/><stop offset="0.55" stop-color="#5a86cf"/><stop offset="0.75" stop-color="#c9c2b3"/><stop offset="1" stop-color="#6f8a4a"/>
      </linearGradient>
      <linearGradient id="trench-site" x1="0" y1="0" x2="1" y2="1">
        <stop offset="0" stop-color="#2f4451"/><stop offset="1" stop-color="#22333f"/>
      </linearGradient>
    </defs>

    <!-- background bands -->
    <polygon points="620,0 760,0 560,601 420,601" fill="var(--light-gray)"/>
    <polygon points="0,574 470,574 452,617 0,617" fill="var(--light-gray)"/>
    <polygon points="0,1025 300,1025 95,1556 0,1556" fill="var(--mid-gray)"/>

    <!-- photo areas -->
    <polygon role="img" aria-label="Photo: excavator digging beside a pickup truck, in grayscale" points="729,0 1100,0 1100,439 565,439" fill="url(#gray-site)"/>
    <polygon role="img" aria-label="Photo: finished concrete septic tank lid in fresh soil with an excavator behind" points="0,328 500,328 435,574 0,574" fill="url(#tank-site)"/>
    <polygon role="img" aria-label="Photo: concrete septic tank being lowered from a truck boom under blue sky" points="565,439 1100,439 1100,1043 420,1043" fill="url(#sky-site)"/>
    <polygon role="img" aria-label="Photo: excavated trench with exposed soil, dark tinted" points="315,1043 1100,1043 1100,1442 158,1442" fill="url(#trench-site)"/>

    <!-- diagonal stripes -->
    <polygon points="712,0 728,0 564,439 548,439" fill="var(--brand-red)"/>
    <polygon points="505,439 540,439 95,1556 55,1556" fill="var(--navy)"/>

    <!-- frame around lowering photo -->
    <polyline points="478,604 968,604 775,1043" fill="none" stroke="var(--white)" stroke-width="12"/>
    <polyline points="488,606 958,606 768,1043" fill="none" stroke="var(--brand-red)" stroke-width="5"/>

    <!-- headline banner -->
    <polygon points="0,617 470,617 310,1025 0,1025" fill="var(--brand-red)"/>
    <polygon points="470,617 945,617 780,1025 310,1025" fill="var(--brand-red)" fill-opacity="0.86"/>

    <!-- frame around trench area -->
    <polyline points="1100,1055 325,1055 170,1442" fill="none" stroke="var(--white)" stroke-width="12"/>
    <polyline points="1100,1062 330,1062 178,1442" fill="none" stroke="var(--brand-red)" stroke-width="5"/>

    <!-- contact bar -->
    <polygon points="170,1442 1100,1442 1100,1556 125,1556" fill="var(--paper)"/>
  </svg>

  <header class="brand">
    <h1 class="brand-name"><span class="line-1">Harlow</span><span class="line-2">Grading &amp; Septic</span></h1>
    <span class="brand-phone">555.214.0187</span>
  </header>

  <h2 class="headline">
    <span class="row"><span class="plain">EXPERT </span><span class="accent">EXCAVATING</span></span>
    <span class="row row-2"><span class="plain">&amp; </span><span class="accent">SEPTIC SOLUTIONS</span></span>
    <span class="row tagline">–YOU CAN TRUST–</span>
  </h2>

  <section class="services">
    <h3 class="services-title">Services Offered:</h3>
    <ul class="service-list">
      <li><svg class="tick" viewBox="0 0 30 28"><path d="M3 15 L11 23 L27 4" fill="none" stroke="var(--signal-yellow)" stroke-width="4"/></svg>Mobile Home Pads</li>
      <li><svg class="tick" viewBox="0 0 30 28"><path d="M3 15 L11 23 L27 4" fill="none" stroke="var(--signal-yellow)" stroke-width="4"/></svg>Meter Pole Placement<br>and Connection</li>
      <li><svg class="tick" viewBox="0 0 30 28"><path d="M3 15 L11 23 L27 4" fill="none" stroke="var(--signal-yellow)" stroke-width="4"/></svg>Waterline Connection</li>
      <li><svg class="tick" viewBox="0 0 30 28"><path d="M3 15 L11 23 L27 4" fill="none" stroke="var(--signal-yellow)" stroke-width="4"/></svg>On Site Septic System Installs</li>
    </ul>
  </section>

  <footer class="contact">
    <svg class="contact-icon" viewBox="0 0 40 40" aria-label="Phone">
      <path d="M10 6 L16 6 L18 14 L14 17 Q17 24 23 27 L26 23 L34 25 L34 31 Q33 35 28 35 Q8 32 5 12 Q5 7 10 6 Z" fill="var(--bright-red)"/>
    </svg>
    <span class="contact-phone">(555) 214-0187</span>
    <svg class="contact-icon" viewBox="0 0 40 40" aria-label="Email">
      <rect x="3" y="9" width="34" height="22" fill="var(--bright-red)"/>
      <path d="M3 9 L20 23 L37 9" fill="none" stroke="var(--white)" stroke-width="2.5"/>
    </svg>
    <span class="contact-web">www.harlowgradingandseptic.com</span>
  </footer>
</main>
</body>
</html>
```